TalkBridge - Language Coaching Services

Sleek, innovative, trendy design for Language Coaching business.

TalkBridge is a new UK based company that provides Language Coaching services. We offer highly personalized on-line and face to face language courses. We also impart learning techniques workshops based on the latest neuroscience research for second-language acquisition.

Target Market(s)

Industry/Entity Type

Consulting

Contact Information for Business Card

TalkBridge
ElenaVT@talkbridge-demo.co.uk
TalkBridge-demo.co.uk
London, UK

Font styles to use
Sans Serif

```html
<!DOCTYPE html>
<html lang="en">
<head>
<meta charset="utf-8">
<title>TalkBridge – Business Card</title>
<link href="https://fonts.googleapis.com/css2?family=Montserrat:wght@300;400;600&display=swap" rel="stylesheet">
<style>
  :root {
    --brand-blue: #1d5f99;
    --brand-deep: #0f4778;
    --ink: #1c1c1c;
    --card-white: #fbfbfa;
    --backdrop: #e6e7e8;
  }
  * { margin: 0; padding: 0; box-sizing: border-box; }
  html, body { width: 1200px; height: 1021px; overflow: hidden; }
  body {
    background: var(--backdrop);
    font-family: "Montserrat", Arial, sans-serif;
    position: relative;
  }
  .card {
    position: absolute;
    width: 560px;
    height: 320px;
    background: var(--card-white);
    border-bottom: 10px solid var(--brand-blue);
    box-shadow: 0 14px 30px rgba(0,0,0,0.18);
    overflow: hidden;
  }
  .card--front { left: 90px; top: 110px; }
  .card--back { left: 550px; top: 590px; }

  .front-ring {
    position: absolute;
    left: 40px;
    top: 40px;
    width: 240px;
    height: 240px;
    border: 16px solid var(--brand-deep);
    border-radius: 50%;
  }
  .front-name {
    position: absolute;
    left: 310px;
    top: 142px;
    font-size: 30px;
    font-weight: 400;
    letter-spacing: 2px;
    color: var(--brand-blue);
  }

  .back-brand {
    position: absolute;
    left: 40px;
    top: 110px;
    width: 210px;
    text-align: center;
  }
  .back-ring {
    width: 76px;
    height: 76px;
    margin: 0 auto 14px;
    border: 6px solid var(--brand-deep);
    border-radius: 50%;
  }
  .back-name {
    font-size: 22px;
    font-weight: 400;
    letter-spacing: 1.5px;
    color: var(--brand-blue);
  }

  .contact {
    position: absolute;
    left: 270px;
    top: 92px;
  }
  .contact-person {
    font-size: 24px;
    font-weight: 300;
    color: var(--ink);
    margin-bottom: 14px;
    letter-spacing: 0.5px;
  }
  .contact-person strong { font-weight: 600; }
  .contact-list { list-style: none; }
  .contact-item {
    display: flex;
    align-items: center;
    gap: 10px;
    font-size: 13px;
    color: var(--ink);
    margin-bottom: 9px;
    padding-left: 26px;
  }
  .contact-item svg { width: 14px; height: 14px; fill: var(--brand-blue); flex: none; }
</style>
</head>
<body>
  <section class="card card--front" aria-label="Card front">
    <div class="front-ring"></div>
    <div class="front-name">TALKBRIDGE</div>
  </section>

  <section class="card card--back" aria-label="Card back">
    <div class="back-brand">
      <div class="back-ring"></div>
      <div class="back-name">TALKBRIDGE</div>
    </div>
    <div class="contact">
      <p class="contact-person">YOUR <strong>NAME</strong></p>
      <ul class="contact-list">
        <li class="contact-item">
          <svg viewBox="0 0 16 16"><path d="M1 3h14v10H1z"/><path d="M1 3l7 6 7-6" fill="none" stroke="#fff" stroke-width="1.4"/></svg>
          ElenaVT@talkbridge-demo.co.uk
        </li>
        <li class="contact-item">
          <svg viewBox="0 0 16 16"><circle cx="8" cy="8" r="7"/><path d="M1 8h14M8 1c-3 3-3 11 0 14M8 1c3 3 3 11 0 14" fill="none" stroke="#fff" stroke-width="1"/></svg>
          TalkBridge-demo.co.uk
        </li>
        <li class="contact-item">
          <svg viewBox="0 0 16 16"><path d="M8 1a5 5 0 0 0-5 5c0 4 5 9 5 9s5-5 5-9a5 5 0 0 0-5-5z"/><circle cx="8" cy="6" r="2" fill="#fff"/></svg>
          London, UK
        </li>
      </ul>
    </div>
  </section>
</body>
</html>
```